business card double side design

We need a business card design for our company BRIGHTlearn. DOUBLE SIDED. We provide continuing education programs & courses across North America. Our website is www.brightlearn-example.com - please use the grey pinstrip concept as part of the design. Compliment the branding that is occuring on that site!
Please use pantones daa520 and 3f3151. Verdana for text. I have attached our logo.
I would like the logo & website address www.BRIGHTlearn-example.com on the front of the card, all other info on the backside. The final design should communicate authority and credibility.

Industry/Entity Type

Professional Service

Font styles to use
Other font styles liked:
• verdanda

Requirements
Must have
• pantones daa520 and 3f3151. Verdana for text.
• must compliment the branding occuring on the www.BRIGHTlearn-example.com

```html
<!DOCTYPE html>
<html lang="en">
<head>
<meta charset="utf-8">
<title>BRIGHTlearn business card – back and front</title>
<link rel="stylesheet" href="https://fonts.googleapis.com/css2?family=Noto+Sans:wght@400;700&display=swap">
<style>
  :root {
    --gold: #daa520;
    --gold-deep: #b8861a;
    --ink: #0f0f10;
    --card-dark: #161617;
    --card-mid: #2a2a2c;
    --white: #ffffff;
    --soft-white: #e9e9e9;
    --backdrop: #3b3431;
    --seal-tint: rgba(218, 165, 32, 0.08);
  }
  * { box-sizing: border-box; margin: 0; padding: 0; }
  html, body { width: 1200px; height: 844px; overflow: hidden; }
  body {
    background: var(--backdrop);
    font-family: "Noto Sans", Verdana, sans-serif;
    position: relative;
  }
  .card {
    position: absolute;
    width: 525px;
    height: 300px;
    overflow: hidden;
    border-radius: 3px;
    box-shadow: 0 14px 30px rgba(0, 0, 0, 0.45);
  }

  /* Back side */
  .card-back {
    left: 50px;
    top: 272px;
    background: linear-gradient(100deg, var(--ink) 0%, var(--card-dark) 55%, var(--card-mid) 100%);
  }
  .gold-band {
    position: absolute;
    left: 0;
    width: 100%;
    height: 13px;
    background: var(--gold);
  }
  .gold-band.top { top: 12px; }
  .gold-band.bottom { bottom: 12px; }
  .seal-watermark {
    position: absolute;
    left: 120px;
    top: 40px;
    width: 230px;
    height: 230px;
    border-radius: 50%;
    background: var(--seal-tint);
    border: 16px solid rgba(0, 0, 0, 0.25);
  }
  .contact-block {
    position: absolute;
    left: 215px;
    top: 62px;
    width: 230px;
    text-align: center;
    color: var(--white);
  }
  .person-name {
    display: inline-block;
    font-weight: 700;
    font-size: 19px;
    letter-spacing: 1px;
    text-transform: uppercase;
    padding: 0 6px 3px;
    border-bottom: 1px solid var(--gold);
  }
  .person-title {
    font-size: 13px;
    color: var(--soft-white);
    margin-top: 4px;
  }
  .contact-lines {
    list-style: none;
    margin-top: 36px;
    font-size: 14px;
    line-height: 20px;
    color: var(--soft-white);
  }
  .social-row {
    display: flex;
    justify-content: center;
    gap: 8px;
    margin-top: 16px;
  }
  .social-slot {
    width: 20px;
    height: 20px;
    border-radius: 3px;
    background: var(--white);
  }

  /* Front side */
  .card-front {
    left: 625px;
    top: 272px;
    background: radial-gradient(ellipse at 55% 35%, #323234 0%, var(--card-dark) 55%, var(--ink) 100%);
  }
  .edge-tab {
    position: absolute;
    width: 26px;
    height: 26px;
    background: linear-gradient(90deg, var(--soft-white) 0 3px, var(--gold) 3px);
  }
  .edge-tab.upper { right: 16px; top: 16px; background: linear-gradient(90deg, var(--gold) 0 23px, var(--soft-white) 23px); }
  .edge-tab.lower { left: 90px; bottom: 16px; }
  .brand {
    position: absolute;
    left: 0;
    right: 0;
    top: 100px;
    display: flex;
    align-items: center;
    justify-content: center;
    gap: 14px;
  }
  .brand-mark {
    width: 62px;
    height: 62px;
    border-radius: 50%;
    background: var(--gold);
  }
  .brand-name {
    font-weight: 700;
    font-size: 38px;
    color: var(--gold);
    letter-spacing: 0.5px;
  }
  .website {
    position: absolute;
    left: 0;
    right: 0;
    top: 196px;
    text-align: center;
    font-weight: 700;
    font-size: 15px;
    color: var(--gold);
    letter-spacing: 0.3px;
  }
</style>
</head>
<body>

  <section class="card card-back" aria-label="Card back">
    <div class="gold-band top"></div>
    <div class="seal-watermark" role="img" aria-label="Faint brand seal decoration"></div>
    <div class="contact-block">
      <h1 class="person-name">Dana Whitfield</h1>
      <p class="person-title">Founder/CEO</p>
      <ul class="contact-lines">
        <li>555.014.2371</li>
        <li>555.019.8846</li>
        <li>dana@BRIGHTlearn-example.com</li>
      </ul>
      <div class="social-row" aria-label="Social profiles">
        <span class="social-slot"></span>
        <span class="social-slot"></span>
        <span class="social-slot"></span>
      </div>
    </div>
    <div class="gold-band bottom"></div>
  </section>

  <section class="card card-front" aria-label="Card front">
    <div class="edge-tab upper"></div>
    <div class="brand">
      <span class="brand-mark" aria-hidden="true"></span>
      <span class="brand-name">BRIGHTlearn</span>
    </div>
    <p class="website">www.BRIGHTlearn-example.com</p>
    <div class="edge-tab lower"></div>
  </section>

</body>
</html>
```